We need 3 A2 posters similar look but different enough to be eye catching when changed.

We are a healthcare centre that requires 3 A2 posters - simple, similar but different background colours. These posters will be used within our business to promote services we provide to our clients.

The design should include our logo(attached), a large header and a large section in the middle of the poster to promote the event. We need a blank text box (which WE can insert text to advertise), and 1 image to advertise the event. Please note, we do not need you to choose an image we simply would like you to place a demo to give us an idea of where it should sit.

We want to use the bubble design (attached) as a background and the company colours pink, orange and blue - as on our website. Attached is a copy of our logo and background bubble effect. You can also refer to our website - www.marlowpinegroup.com.au for more inspiration.

Just to reiterate, these posters should be simple, different but have a uniform feel. They should have an empty middle section that can be edited to add text and a space for an eye catching title and matching image.

Our services include Chiropractic, Podiatry, Nutrition, Massage, Yoga, Pilates and Specialised rehabilitation classes.

Reason: Hi designers, I know we are all busy but I really need more designs from the designers I invited to this project and look forward to receiving more designs. Any questions please let me know. Regards, Noreen

Reason: Hi all Increased the budget Regards Noreen

Target Market(s)

Corporate Sydney City office workers

Industry/Entity Type

Healthcare

Requirements
Must have
• logo and company colours
section in the middles that can be edited to add text
Space allocated for image placement
Catchy title/header

```html
<!DOCTYPE html>
<html lang="en">
<head>
<meta charset="utf-8">
<title>Marlow Pine Health – Poster Series</title>
<link rel="stylesheet" href="https://fonts.googleapis.com/css2?family=Open+Sans:ital,wght@0,300;0,400;0,700;1,300;1,700&family=Carlito:ital,wght@0,400;0,700;1,400;1,700&display=swap">
<style>
  :root{
    --pink:#b5177f;
    --orange:#e87511;
    --blue:#0a7cc1;
    --ink:#2f2f2f;
    --grey:#8a8a8a;
    --rule:#b9b9b9;
    --paper:#ffffff;
    --sheet:#f4f4f4;
  }
  *{box-sizing:border-box;margin:0;padding:0}
  html,body{width:1200px;height:533px;overflow:hidden;background:#fff}
  .canvas{position:relative;width:1200px;height:533px;background:#fff}

  .poster{position:absolute;top:0;width:376px;height:533px;border:1px solid #d9d9d9;overflow:hidden;
    font-family:"Open Sans",Arial,sans-serif;color:var(--ink)}
  .poster--one{left:3px;--name:var(--pink);--accent:var(--orange);--footer:var(--blue)}
  .poster--two{left:408px;--name:var(--blue);--accent:var(--pink);--footer:var(--orange)}
  .poster--three{left:824px;--name:var(--orange);--accent:var(--blue);--footer:var(--pink)}

  .bubble-field{position:absolute;inset:0;
    background:radial-gradient(circle at 30% 20%,#e6e6e6 0,#f7f7f7 40%,#fff 70%),var(--sheet);
    opacity:.9}

  .brand{position:absolute;top:6px;left:8px;display:flex;align-items:center;gap:6px}
  .brand__mark{width:14px;height:14px;background:var(--accent)}
  .brand__name{font-family:"Open Sans",Arial,sans-serif;font-weight:700;font-size:17px;color:var(--ink);white-space:nowrap}

  .doctors{position:absolute;top:80px;left:6px;display:flex;align-items:flex-end}
  .doctors__title{font-family:"Carlito",Calibri,sans-serif;font-size:42px;line-height:40px;color:transparent;
    -webkit-text-stroke:1px #9a9a9a}
  .doctors__names{margin-left:3px;background:var(--name);color:#fff;height:44px;padding:0 8px;
    font-family:"Carlito",Calibri,sans-serif;font-weight:700;font-size:29px;line-height:50px;white-space:nowrap}
  .doctors__names .amp{color:var(--ink);font-weight:400}

  .tagline{position:absolute;top:135px;left:75px;width:296px;height:30px;border-top:1px solid var(--rule);
    border-bottom:1px solid var(--rule);font-style:italic;white-space:nowrap}
  .tagline__soft{font-weight:300;font-size:17px;color:var(--grey);letter-spacing:2px}
  .tagline__strong{font-weight:700;font-size:22px;color:var(--ink);letter-spacing:3px}

  .feature{position:absolute;top:190px;left:12px;width:350px;height:156px;background:var(--paper);
    box-shadow:2px 3px 6px rgba(0,0,0,.35);overflow:hidden}
  .feature__brand{position:absolute;display:flex;align-items:center;gap:3px}
  .feature__brand .brand__mark{width:7px;height:7px}
  .feature__brand .brand__name{font-size:9px}
  .photo{position:absolute;background:linear-gradient(135deg,#f2f2f0,#d8d6d2 60%,#9c9a98)}
  .points{position:absolute;list-style:none;font-size:5.4px;line-height:6.6px}
  .points li{position:relative;padding-left:8px;margin-bottom:4px}
  .points li::before{content:"";position:absolute;left:0;top:1px;width:4px;height:4px;border:1px solid currentColor}
  .slogan{position:absolute;font-family:"Carlito",Calibri,sans-serif;white-space:nowrap;color:var(--ink)}
  .slogan__big{font-size:19px}
  .slogan__small{font-size:12px}
  .programme{position:absolute;font-family:"Carlito",Calibri,sans-serif;font-size:26px;line-height:28px;color:var(--accent);white-space:nowrap}
  .programme small{font-size:11px}

  .feature--one .panel{position:absolute;left:5px;top:24px;width:337px;height:90px;background:var(--orange)}
  .feature--one .points{color:#fff;width:86px;top:40px}
  .feature--two .band{position:absolute;left:0;top:0;width:350px;height:57px;background:var(--pink)}
  .feature--two .band::after{content:"";position:absolute;left:0;top:20px;width:350px;height:37px;background:#c04a98}
  .feature--three .panel{position:absolute;left:0;top:0;width:178px;height:156px;background:var(--blue)}
  .feature--three .slogan__big{font-size:15px}
  .feature--three .slogan__small{font-size:10px}

  .services__label{position:absolute;top:364px;left:190px;width:128px;height:19px;border:1px solid var(--ink);background:#fff;
    font-weight:700;font-style:italic;font-size:15px;line-height:17px;letter-spacing:3px;text-align:center}
  .service{position:absolute;background:var(--accent);color:#fff;font-size:9px;font-weight:700;line-height:16px;
    padding:0 3px;box-shadow:1px 1px 2px rgba(0,0,0,.35);white-space:nowrap}
  .service--chiro{left:33px;top:364px;width:65px}
  .service--podiatry{left:91px;top:391px;width:46px}
  .service--massage{left:174px;top:402px;width:45px}
  .service--nutrition{left:121px;top:418px;width:46px}
  .service--yoga{left:208px;top:427px;width:28px}
  .service--pilates{left:234px;top:453px;width:34px}
  .service--rehab{left:280px;top:435px;width:67px;height:41px;line-height:13px;padding-top:2px;white-space:normal}

  .footer{position:absolute;left:26px;top:516px;width:328px;height:15px;background:var(--footer);color:#fff;
    font-weight:700;font-style:italic;font-size:9px;line-height:15px;letter-spacing:2.6px;text-align:center;white-space:nowrap}
</style>
</head>
<body>
<main class="canvas">

  <section class="poster poster--one">
    <div class="bubble-field" role="img" aria-label="Soft grey bubble background pattern"></div>
    <div class="brand"><span class="brand__mark"></span><span class="brand__name">Marlow Pine Health</span></div>
    <div class="doctors"><span class="doctors__title">Drs</span><span class="doctors__names">Noreen <span class="amp">&amp;</span> Tomas</span></div>
    <p class="tagline"><span class="tagline__soft">give a </span><span class="tagline__strong">special care</span><span class="tagline__soft"> to you</span></p>
    <div class="feature feature--one">
      <div class="feature__brand" style="left:4px;top:6px"><span class="brand__mark"></span><span class="brand__name">Marlow Pine Health</span></div>
      <div class="panel"></div>
      <div class="photo" style="left:104px;top:28px;width:136px;height:84px" role="img" aria-label="Placeholder photo of a woman in a yoga stretch"></div>
      <ul class="points" style="left:10px">
        <li>Is run by health professionals, making sure you stay injury free and achieve your maximum potential during your workouts</li>
        <li>Will always have a limited number of participants per class</li>
      </ul>
      <ul class="points" style="left:246px;width:90px">
        <li>Has only the best instructors in Sydney, selected for their education, knowledge, experience and ability</li>
        <li>Boasts an extensive timetable with convenient options designed to suit all availabilities</li>
      </ul>
      <p class="slogan" style="left:18px;top:126px"><span class="slogan__big">nature </span><span class="slogan__small">therapies </span><span class="slogan__big">to </span><span class="slogan__small">keep </span><span class="slogan__big">you</span></p>
      <p class="programme" style="right:8px;top:122px">strong<small>&amp;</small>well</p>
    </div>
    <p class="services__label">Our services</p>
    <span class="service service--chiro">Chiropractic</span>
    <span class="service service--podiatry">Podiatry</span>
    <span class="service service--massage">Massage</span>
    <span class="service service--nutrition">Nutrition</span>
    <span class="service service--yoga">Yoga</span>
    <span class="service service--pilates">Pilates</span>
    <span class="service service--rehab">Specialised rehabilitation classes</span>
    <p class="footer">One place for a complete health solution</p>
  </section>

  <section class="poster poster--two">
    <div class="bubble-field" role="img" aria-label="Soft grey bubble background pattern"></div>
    <div class="brand"><span class="brand__mark"></span><span class="brand__name">Marlow Pine Health</span></div>
    <div class="doctors"><span class="doctors__title">Drs</span><span class="doctors__names">Noreen <span class="amp">&amp;</span> Tomas</span></div>
    <p class="tagline"><span class="tagline__soft">give a </span><span class="tagline__strong">special care</span><span class="tagline__soft"> to you</span></p>
    <div class="feature feature--two">
      <div class="band"></div>
      <div class="feature__brand" style="left:214px;top:6px"><span class="brand__mark" style="background:#fff"></span><span class="brand__name" style="color:#fff">Marlow Pine Health</span></div>
      <p class="slogan" style="left:4px;top:34px;color:#fff"><span class="slogan__big">nature </span><span class="slogan__small">therapies </span><span class="slogan__big">to </span><span class="slogan__small">keep </span><span class="slogan__big">you</span></p>
      <ul class="points" style="left:8px;top:64px;width:188px">
        <li>Is run by health professionals, making sure you stay injury free and achieve your maximum potential during your workouts</li>
        <li>Will always have a limited number of participants per class</li>
        <li>Has only the best instructors in Sydney, selected for their education, knowledge, experience and ability</li>
        <li>Boasts an extensive timetable with convenient options designed to suit all availabilities</li>
      </ul>
      <div class="photo" style="left:203px;top:60px;width:147px;height:96px" role="img" aria-label="Placeholder photo of a woman in a yoga stretch"></div>
      <p class="programme" style="left:68px;top:122px">strong<small>&amp;</small>well</p>
    </div>
    <p class="services__label">Our services</p>
    <span class="service service--chiro">Chiropractic</span>
    <span class="service service--podiatry">Podiatry</span>
    <span class="service service--massage">Massage</span>
    <span class="service service--nutrition">Nutrition</span>
    <span class="service service--yoga">Yoga</span>
    <span class="service service--pilates">Pilates</span>
    <span class="service service--rehab">Specialised rehabilitation classes</span>
    <p class="footer">One place for a complete health solution</p>
  </section>

  <section class="poster poster--three">
    <div class="bubble-field" role="img" aria-label="Soft grey bubble background pattern"></div>
    <div class="brand"><span class="brand__mark"></span><span class="brand__name">Marlow Pine Health</span></div>
    <div class="doctors"><span class="doctors__title">Drs</span><span class="doctors__names">Noreen <span class="amp">&amp;</span> Tomas</span></div>
    <p class="tagline"><span class="tagline__soft">give a </span><span class="tagline__strong">special care</span><span class="tagline__soft"> to you</span></p>
    <div class="feature feature--three">
      <div class="panel"></div>
      <p class="slogan" style="left:5px;top:8px;color:#fff"><span class="slogan__big">nature </span><span class="slogan__small">therapies </span><span class="slogan__big">to </span><span class="slogan__small">keep </span><span class="slogan__big">you</span></p>
      <div style="position:absolute;left:9px;top:34px;width:160px;height:102px;border:2px solid #fff"></div>
      <div class="photo" style="left:14px;top:39px;width:150px;height:92px" role="img" aria-label="Placeholder photo of a woman in a yoga stretch"></div>
      <div class="feature__brand" style="left:6px;top:142px"><span class="brand__mark" style="background:#fff"></span><span class="brand__name" style="color:#fff">Marlow Pine Health</span></div>
      <p class="programme" style="left:205px;top:12px">strong<small>&amp;</small>well</p>
      <ul class="points" style="left:184px;top:52px;width:160px;text-align:center">
        <li>Is run by health professionals, making sure you stay injury free and achieve your maximum potential during your workouts</li>
        <li>Will always have a limited number of participants per class</li>
        <li>Has only the best instructors in Sydney, selected for their education, knowledge, experience and ability</li>
        <li>Boasts an extensive timetable with convenient options designed to suit all availabilities</li>
      </ul>
    </div>
    <p class="services__label">Our services</p>
    <span class="service service--chiro">Chiropractic</span>
    <span class="service service--podiatry">Podiatry</span>
    <span class="service service--massage">Massage</span>
    <span class="service service--nutrition">Nutrition</span>
    <span class="service service--yoga">Yoga</span>
    <span class="service service--pilates">Pilates</span>
    <span class="service service--rehab">Specialised rehabilitation classes</span>
    <p class="footer">One place for a complete health solution</p>
  </section>

</main>
</body>
</html>
```